CREATE A KILLER WEBSITE DESIGN

We are a firearms training company that trains CIVILIANS (no police or military pictures - thank you!) to defend themselves and are looking for a killer design that's clean, easy to navigate and modern! We want the newest trends applied to this sight like a scrollable site so you can scroll down and see all the features. We are okay with tweaking the HTML but need the artistic design to look good. I'll provide a link to our current site along with a sight we really like so you can get an idea!

I'm supplying a PowerPoint Design we are going with from another designer so you can match the style to the new site.

PAGES: (Please use information from our current site. We like the information but just want a more polished look similar to the NWDLA site below but in our colors.)
Home - Long Form Scrolling Site. Top fold will be a video with a play button.
Falcon Institute - Seven Level Training Program Info Page That Will Contain A Video.
Contact Us - This will be a page that DOES NOT CONTAIN AN EMAIL ADDRESS. Just a contact us form
Meet The Trainer: Morgan Pellbrook

Our site:
https://www.brisklanewardens.biz

Sights We Like:
https://www.nwdefenseleague.example.com
https://quorvel.example.com
https://brantforgeworks.example.com
https://www.pelnrigear.example.com

Target Market(s)

Men and women ages 21 to 100 years old

Industry/Entity Type

Self Defense

Number of Pages Required

5+ page

Font styles to use
Sans Serif

Colors
f26267

Requirements
Must have
• Clean and engaging. Use of colors that match our logo.
Should not have
• Poor design quality

```html
<!DOCTYPE html>
<html lang="en">
<head>
<meta charset="utf-8">
<title>Brisklane Wardens – Home &amp; Sitemap</title>
<link href="https://fonts.googleapis.com/css2?family=Montserrat:wght@300;400;500;600;700;800&display=swap" rel="stylesheet">
<style>
  :root{
    --brand-red:#e0595e;
    --brand-red-bright:#f26267;
    --header-black:#000000;
    --white:#ffffff;
    --ink:#2b2b2b;
    --hero-deep:#1f4a47;
    --hero-mid:#3c6b67;
    --hero-glow:#e9f1da;
    --rule:#444444;
  }
  *{margin:0;padding:0;box-sizing:border-box}
  html,body{width:1200px;height:987px;overflow:hidden;background:var(--white)}
  body{position:relative;font-family:"Montserrat",sans-serif;color:var(--ink)}

  .site-frame{position:absolute;left:54px;top:82px;width:1084px;height:622px;border-radius:12px;overflow:hidden;box-shadow:4px 8px 14px rgba(0,0,0,.35);background:var(--header-black)}

  .site-header{position:absolute;left:0;top:0;width:100%;height:90px;background:var(--header-black)}
  .brand{position:absolute;left:84px;top:18px;width:90px;display:flex;flex-direction:column;align-items:center;gap:5px}
  .brand-dot{width:30px;height:30px;border-radius:50%;background:var(--brand-red-bright)}
  .brand-name{font-weight:700;font-size:11px;line-height:12px;color:var(--white);text-align:center;letter-spacing:.5px}
  .tagline{position:absolute;left:199px;top:23px;font-family:"Montserrat",sans-serif;font-weight:600;font-size:13.5px;letter-spacing:1.9px;color:var(--white);white-space:nowrap}
  .header-rule{position:absolute;left:199px;top:45px;width:800px;height:1px;background:var(--rule)}
  .utility{position:absolute;top:24px;display:flex;align-items:center;gap:4px;font-size:10.5px;font-weight:600}
  .utility.cart{left:896px;color:var(--white)}
  .utility.login{left:961px;color:var(--brand-red-bright)}
  .main-nav{position:absolute;left:199px;top:60px;display:flex;font-size:12.5px;font-weight:600;letter-spacing:.6px;color:var(--white)}
  .main-nav a{color:inherit;text-decoration:none;position:relative;white-space:nowrap;margin-right:34px}
  .main-nav .lost{margin-right:0}
  .main-nav .home::before{content:"";position:absolute;left:7px;top:-5px;width:22px;height:22px;border-radius:50%;border:2px solid rgba(224,89,94,.7);z-index:-1}
  .header-cta{position:absolute;left:808px;top:53px;width:191px;height:29px;background:var(--brand-red);color:var(--white);font-size:12px;font-weight:600;letter-spacing:.7px;display:flex;align-items:center;justify-content:center}

  .hero{position:absolute;left:0;top:90px;width:100%;height:532px}
  .hero-media{position:absolute;inset:0;background:
      radial-gradient(ellipse 260px 200px at 90% 50%, var(--hero-glow) 0%, rgba(233,241,218,.5) 35%, rgba(233,241,218,0) 75%),
      linear-gradient(180deg,var(--hero-mid) 0%,#2d5d59 55%,var(--hero-deep) 100%)}
  .hero-title{position:absolute;left:0;width:100%;top:162px;text-align:center;font-weight:800;font-size:40px;line-height:39px;color:var(--white);letter-spacing:.3px}
  .hero-sub{position:absolute;left:0;width:100%;top:255px;padding-left:14px;text-align:center;font-weight:300;font-size:16px;letter-spacing:.4px;color:var(--white)}
  .btn{position:absolute;left:352px;width:213px;height:40px;display:flex;align-items:center;justify-content:center;font-size:12px;font-weight:600;letter-spacing:.6px;color:var(--white)}
  .btn-primary{top:316px;background:var(--brand-red)}
  .btn-outline{top:364px;border:1.5px solid var(--brand-red)}
  .hero-divider{position:absolute;left:610px;top:301px;width:1px;height:126px;background:var(--white)}
  .play-film{position:absolute;left:645px;top:313px;width:80px;text-align:center}
  .play-film svg{display:block;margin:0 auto}
  .play-label{margin-top:8px;font-size:12.5px;font-weight:600;letter-spacing:.6px;color:var(--white)}

  .sitemap{position:absolute;left:0;top:780px;width:100%}
  .sitemap-col{position:absolute;top:0}
  .sitemap-head{font-weight:600;font-size:27px;letter-spacing:.5px;color:var(--ink);white-space:nowrap}
  .sitemap-sub{position:absolute;top:40px;border-left:1.5px solid var(--ink);padding-left:9px;font-weight:600;font-size:15.5px;line-height:20.5px;white-space:nowrap}
  .col-home{left:85px}
  .col-about{left:221px}
  .col-about .sitemap-sub{left:8px}
  .col-institute{left:373px}
  .col-institute .sitemap-sub{left:10px}
  .col-shop{left:710px}
  .col-lost{left:841px}
</style>
</head>
<body>

<div class="site-frame">
  <header class="site-header">
    <div class="brand">
      <span class="brand-dot"></span>
      <span class="brand-name">BRISKLANE WARDENS</span>
    </div>
    <div class="tagline">PREPARED TO PREVAIL</div>
    <div class="utility cart">
      <svg width="16" height="13" viewBox="0 0 16 13" fill="none" stroke="#fff" stroke-width="1.3"><path d="M1 1h3l2 7h7l2-5H5"/><circle cx="7" cy="11" r="1"/><circle cx="12" cy="11" r="1"/></svg>
      <span>&nbsp;0</span>
    </div>
    <div class="utility login">LOG IN</div>
    <div class="header-rule"></div>
    <nav class="main-nav">
      <a class="home" href="#">HOME</a>
      <a class="about" href="#">ABOUT</a>
      <a class="institute" href="#">FALCON INSTITUTE</a>
      <a class="shop" href="#">SHOP</a>
      <a class="lost" href="#">LOST CERTIFICATE</a>
    </nav>
    <div class="header-cta">JOIN FALCON INSTITUTE</div>
  </header>

  <section class="hero">
    <div class="hero-media" role="img" aria-label="Background video still: a bullet leaving a muzzle in slow motion with a bright flash on the right"></div>
    <h1 class="hero-title">Don't Settle For A<br>Gun Shop Class!</h1>
    <p class="hero-sub">Your life may depend on what you learn in your concealed training</p>
    <a class="btn btn-primary">JOIN FALCON INSTITUTE</a>
    <a class="btn btn-outline">GET TICKETS NOW</a>
    <div class="hero-divider"></div>
    <div class="play-film">
      <svg width="70" height="70" viewBox="0 0 70 70">
        <line x1="35" y1="1" x2="35" y2="69" stroke="#e0595e" stroke-width="1.5"/>
        <line x1="1" y1="35" x2="69" y2="35" stroke="#e0595e" stroke-width="1.5"/>
        <circle cx="35" cy="35" r="29" fill="none" stroke="#e0595e" stroke-width="3"/>
        <circle cx="35" cy="35" r="23" fill="none" stroke="#e0595e" stroke-width="2"/>
        <circle cx="35" cy="35" r="18" fill="#e0595e"/>
        <path d="M29 25 L45 35 L29 45 Z" fill="#fff"/>
      </svg>
      <div class="play-label">PLAY FILM</div>
    </div>
  </section>
</div>

<section class="sitemap">
  <div class="sitemap-col col-home"><div class="sitemap-head">HOME</div></div>
  <div class="sitemap-col col-about">
    <div class="sitemap-head">ABOUT</div>
    <div class="sitemap-sub">The Instructor<br>Testimonials<br>Videos</div>
  </div>
  <div class="sitemap-col col-institute">
    <div class="sitemap-head">FALCON INSTITUTE</div>
    <div class="sitemap-sub">Join Falcon Institute<br>Upcoming Classes</div>
  </div>
  <div class="sitemap-col col-shop"><div class="sitemap-head">SHOP</div></div>
  <div class="sitemap-col col-lost"><div class="sitemap-head">LOST CERTIFICATE</div></div>
</section>

</body>
</html>
```